Love pets? Create a veterinary business card that aligns with our new revamped website.

Greetings! We are a five-doctor veterinary hospital that seeks your expertise in designing a new business card that harmonizes with our recently revitalized website: www.tqrn.net. The card should feature our logo, the five doctors, operating hours, contact information, and communicate our purpose and personality.

Contact Information for Business Card

TBA

```html
<!DOCTYPE html>
<html lang="en">
<head>
<meta charset="utf-8">
<title>Maple Hollow Veterinary Hospital – Business Card</title>
<link href="https://fonts.googleapis.com/css2?family=Dancing+Script:wght@500&family=Roboto:wght@300;400;700&display=swap" rel="stylesheet">
<style>
  :root {
    --backdrop: #d9d9d9;
    --card: #eef0f2;
    --slate: #7a9ba8;
    --slate-soft: #a9c0c9;
    --ink-light: #ffffff;
  }
  * { box-sizing: border-box; margin: 0; padding: 0; }
  html, body { width: 1200px; height: 846px; overflow: hidden; }
  body {
    background: var(--backdrop);
    font-family: "Roboto", sans-serif;
    color: var(--slate);
    position: relative;
  }
  .card {
    position: absolute;
    top: 268px;
    width: 540px;
    height: 310px;
    background: var(--card);
    overflow: hidden;
  }
  .card--front { left: 40px; }
  .card--back { left: 620px; }

  .brand {
    position: absolute;
    display: flex;
    align-items: center;
    gap: 10px;
    font-family: "Roboto", sans-serif;
    font-weight: 400;
    color: var(--slate);
  }
  .brand__dot {
    width: 34px; height: 34px;
    border-radius: 50%;
    background: var(--slate);
    flex: none;
  }
  .brand__name { font-size: 17px; line-height: 1.15; letter-spacing: .3px; }

  .card--front .brand { left: 30px; top: 36px; }
  .person {
    position: absolute;
    left: 30px; top: 92px;
    font-family: "Dancing Script", cursive;
    font-weight: 500;
    font-size: 34px;
  }
  .contact-list {
    position: absolute;
    left: 34px; top: 148px;
    list-style: none;
    font-size: 15px;
    font-weight: 300;
    line-height: 22px;
  }
  .contact-list li { display: flex; align-items: center; gap: 9px; }
  .contact-list svg { width: 14px; height: 14px; fill: var(--slate); flex: none; }
  .contact-list .address { padding-left: 23px; line-height: 19px; margin-top: 3px; }

  .tree-art {
    position: absolute;
    right: 22px; top: 26px;
    width: 250px; height: 262px;
    background: radial-gradient(ellipse at 50% 42%, var(--slate) 0 58%, rgba(122,155,168,0) 72%);
  }

  .card--back .brand { left: 30px; top: 40px; }
  .grain-art {
    position: absolute;
    left: 0; right: 0; top: 110px; bottom: 0;
    background: linear-gradient(to bottom, var(--slate-soft) 0%, var(--slate) 38%, var(--slate) 100%);
  }
  .hours {
    position: absolute;
    left: 30px; right: 30px; top: 160px;
    color: var(--ink-light);
  }
  .hours__title {
    font-family: "Dancing Script", cursive;
    font-weight: 500;
    font-size: 36px;
    text-align: center;
    margin-bottom: 14px;
  }
  .hours__grid { display: flex; justify-content: space-between; }
  .hours__day { font-weight: 700; font-size: 14px; text-transform: uppercase; letter-spacing: .3px; }
  .hours__time { font-weight: 300; font-size: 15px; margin-top: 2px; }
</style>
</head>
<body>

<section class="card card--front">
  <div class="brand">
    <span class="brand__dot"></span>
    <span class="brand__name">Maple Hollow<br>Veterinary Hospital</span>
  </div>
  <h1 class="person">Name Lastname</h1>
  <ul class="contact-list">
    <li><svg viewBox="0 0 24 24"><path d="M6.6 10.8a15 15 0 0 0 6.6 6.6l2.2-2.2a1 1 0 0 1 1-.25 11.4 11.4 0 0 0 3.6.57 1 1 0 0 1 1 1V20a1 1 0 0 1-1 1A17 17 0 0 1 3 4a1 1 0 0 1 1-1h3.5a1 1 0 0 1 1 1c0 1.25.2 2.45.57 3.57a1 1 0 0 1-.25 1z"/></svg>(555) 214-0198</li>
    <li><svg viewBox="0 0 24 24"><path d="M7 2h8l3 3v5H7zM4 11h16a2 2 0 0 1 2 2v8H2v-8a2 2 0 0 1 2-2zm3 4v2h10v-2z"/></svg>(555) 214-0277</li>
    <li><svg viewBox="0 0 24 24"><path d="M2 5h20v14H2zm2 2v.5l8 5.5 8-5.5V7l-8 5.5z"/></svg>info@tqrn.net</li>
    <li><svg viewBox="0 0 24 24"><path d="M12 2a10 10 0 1 0 0 20 10 10 0 0 0 0-20zm-1 2.1V8H7.3A8 8 0 0 1 11 4.1zm2 0A8 8 0 0 1 16.7 8H13zM4.6 10H11v4H4.6a8 8 0 0 1 0-4zm8.4 0h6.4a8 8 0 0 1 0 4H13zM7.3 16H11v3.9A8 8 0 0 1 7.3 16zm5.7 0h3.7a8 8 0 0 1-3.7 3.9z"/></svg>www.tqrn.net</li>
    <li class="address">4820 Birchwood Lane,<br>Cedar Falls, TX 75001</li>
  </ul>
  <div class="tree-art" role="img" aria-label="Illustration of a large leafy tree silhouette"></div>
</section>

<section class="card card--back">
  <div class="brand">
    <span class="brand__dot"></span>
    <span class="brand__name">Maple Hollow<br>Veterinary Hospital</span>
  </div>
  <div class="grain-art" role="img" aria-label="Decorative wood grain texture band"></div>
  <div class="hours">
    <h2 class="hours__title">Hospital Hours</h2>
    <div class="hours__grid">
      <div><p class="hours__day">Monday to Friday:</p><p class="hours__time">7:00am – 6:00pm</p></div>
      <div><p class="hours__day">Saturday:</p><p class="hours__time">8:00am – 12:00pm</p></div>
      <div><p class="hours__day">Sunday:</p><p class="hours__time">CLOSED</p></div>
    </div>
  </div>
</section>

</body>
</html>
```